依頼詳細
店舗のイメージを崩すことなく多くのお客様へテイクアウトを開始したことを認知していただくことが目的となります。
記載項目
【店名】 濃厚豚骨醤油 らぁ麺ひなた
【メニュー】
鶏つけそば ¥830
汁なし担担麺 ¥830
辛い鶏つけそば ¥860円
激辛!汁なし担担麺 ¥860
ねぎとチャーシューの小さな丼 ¥250
温泉卵と豚そぼろの小さな丼 ¥250

【電話番号】03-5812-7406
【住所】東京都港区東山崎5-8-41 コルネ台ビル1階
【Chirpitアカウント】@noodle_hinata
【補足情報】・FoodDashyの加盟店である旨 ・電話で事前注文可能
サイズ
A6
ページ数
片面
希望イメージ
シンプル 複雑
単色 カラフル
暗い 明るい
日常 高級
遊び心 厳粛
未来的 伝統的
女性的 男性的
希望する色
赤系、黄・オレンジ系、無彩色系
補足説明
頂いたデータをプリモアにて発注する予定なので、所定の形式での納品を希望いたします。
味めぐり、Chirpit、Pictoriaなどの写真の転用OKです。
■ 選んだ理由

分かりやすさ、こちらの要望を的確に具体化してくださる柔軟性が決め手となりました。

■ 提案者全員のお礼・コメント

皆様この度たくさんのご提案誠にありがとうございました。
今回ワクモアでの発注にとても満足していますので、次回の販促物デザインも募集させて頂くことがあると思います。その時はどうぞよろしくお願いいたします。

```html
<!DOCTYPE html>
<html lang="ja">
<head>
<meta charset="utf-8">
<title>らぁ麺ひなた テイクアウト</title>
<link href="https://fonts.googleapis.com/css2?family=Dela+Gothic+One&family=Noto+Sans+JP:wght@500;700;900&family=Noto+Serif+JP:wght@900&display=swap" rel="stylesheet">
<style>
:root{
  --red:#d7161b;
  --deep-red:#b30d12;
  --yellow:#ffd400;
  --orange:#ff9a00;
  --black:#141414;
  --cream:#fbf3e4;
  --white:#ffffff;
  --soup:#c9782e;
}
*{margin:0;padding:0;box-sizing:border-box}
html,body{width:853px;height:1200px;overflow:hidden;background:var(--white)}
body{font-family:"Noto Sans JP",sans-serif;color:var(--black)}
.flyer{position:relative;width:853px;height:1200px;overflow:hidden;background:var(--cream)}

.top-bar{position:absolute;left:0;top:0;width:853px;height:128px;background:var(--white);border-bottom:6px solid var(--black)}
.shop-call{position:absolute;left:24px;top:22px;font-family:"Noto Sans JP",sans-serif;font-weight:900;font-size:58px;letter-spacing:2px;color:var(--black)}
.shop-call .particle{font-size:44px}
.places{position:absolute;right:28px;top:10px;display:flex;gap:10px}
.place{background:var(--red);color:var(--white);font-weight:900;font-size:26px;padding:2px 16px;border-radius:22px}
.hot-line{position:absolute;right:28px;top:60px;font-weight:900;font-size:40px;color:var(--red);letter-spacing:1px}

.hero{position:absolute;left:0;top:134px;width:853px;height:224px;background:radial-gradient(circle at 50% 55%,#ef2a20 0%,var(--red) 55%,var(--deep-red) 100%)}
.hero-title{position:absolute;left:0;width:853px;text-align:center;font-family:"Dela Gothic One",sans-serif;color:var(--yellow);-webkit-text-stroke:5px var(--black);paint-order:stroke fill;line-height:1}
.hero-title.line1{top:18px;font-size:92px;letter-spacing:2px}
.hero-title.line2{top:118px;font-size:88px}

.menu-label{position:absolute;left:0;top:358px;width:853px;height:48px;background:var(--black);color:var(--white);text-align:center;font-weight:900;font-size:36px;line-height:48px;letter-spacing:2px}

.feature{position:absolute;left:44px;top:420px;width:765px}
.feature-name{font-family:"Noto Serif JP",serif;font-weight:900;font-size:36px;color:var(--red);border-bottom:3px solid var(--red);width:335px;padding-bottom:4px}
.spec{margin-top:12px;border-collapse:collapse;width:335px}
.spec td{font-size:20px;font-weight:700;padding:4px 0;border-bottom:1px solid #d9c9a8}
.spec .key{width:70px}
.spec .key span{display:inline-block;background:var(--red);color:var(--white);font-size:17px;width:60px;text-align:center;border-radius:3px;padding:1px 0}
.feature-text{margin-top:14px;width:335px;font-size:15px;line-height:1.6;font-weight:500}
.feature-price{margin-top:8px;font-family:"Noto Serif JP",serif;font-weight:900;font-size:62px;color:var(--red);line-height:1}
.feature-price small{font-size:38px}
.feature-photo{position:absolute;left:365px;top:0;width:400px;height:350px;border-radius:6px;background:radial-gradient(circle at 50% 50%,#e6a25a 0%,var(--soup) 45%,#6d3a1a 80%,#f2eee6 82%,#f7f3ec 100%)}

.menu-list{position:absolute;left:44px;top:800px;width:765px;display:grid;grid-template-columns:1fr 1fr;column-gap:34px;row-gap:4px;border-top:2px solid var(--black);padding-top:10px}
.item{display:flex;align-items:flex-end;font-weight:700;font-size:20px;line-height:1.35}
.item .dots{flex:1;border-bottom:2px dotted var(--black);margin:0 6px 7px}
.note{position:absolute;left:44px;top:935px;font-size:13px;font-weight:500;color:#444}

.footer{position:absolute;left:0;top:958px;width:853px;height:242px;background:var(--black);color:var(--white)}
.footer-shop{position:absolute;left:30px;top:16px;font-weight:900;font-size:34px;letter-spacing:1px}
.phone{position:absolute;left:24px;top:70px;display:flex;align-items:center;gap:10px;font-family:"Noto Sans JP",sans-serif;font-weight:900;font-size:74px;color:var(--yellow);letter-spacing:1px;line-height:1}
.partner{position:absolute;right:26px;top:62px;width:180px;height:100px;background:var(--yellow);color:var(--black);border-radius:8px;text-align:center;font-weight:900}
.partner .name{font-size:28px;padding-top:12px}
.partner .sub{font-size:26px}
.address{position:absolute;left:30px;top:190px;font-size:18px;font-weight:700;letter-spacing:.5px}
.preorder{position:absolute;left:30px;top:160px;font-size:18px;font-weight:700;color:var(--yellow)}
</style>
</head>
<body>
<main class="flyer">
  <header class="top-bar">
    <div class="shop-call">らぁ麺ひなた<span class="particle">が</span></div>
    <div class="places"><span class="place">お家で</span><span class="place">オフィスで</span></div>
    <div class="hot-line">アツアツのラーメン!</div>
  </header>

  <section class="hero">
    <h1 class="hero-title line1">テイクアウト</h1>
    <p class="hero-title line2">はじめました!</p>
  </section>

  <div class="menu-label">TAKE OUT MENU</div>

  <section class="feature">
    <h2 class="feature-name">激辛!汁なし担担麺</h2>
    <table class="spec">
      <tr><td class="key"><span>スープ</span></td><td>水炊きスープ</td></tr>
      <tr><td class="key"><span>たれ</span></td><td>担担胡麻たれ</td></tr>
      <tr><td class="key"><span>麺</span></td><td>平打ち麺 200g</td></tr>
    </table>
    <p class="feature-text">人気の汁なし担担麺をお家で楽しめるよう、辛さを増したテイクアウト限定仕様にしました。花椒の香りと胡麻のコクをぜひご自宅で。</p>
    <p class="feature-price">860<small>円</small></p>
    <div class="feature-photo" role="img" aria-label="激辛汁なし担担麺の写真"></div>
  </section>

  <section class="menu-list">
    <div class="item"><span>鶏つけそば</span><span class="dots"></span><span>¥830</span></div>
    <div class="item"><span>ねぎとチャーシューの小さな丼</span><span class="dots"></span><span>¥250</span></div>
    <div class="item"><span>汁なし担担麺</span><span class="dots"></span><span>¥830</span></div>
    <div class="item"><span>温泉卵と豚そぼろの小さな丼</span><span class="dots"></span><span>¥250</span></div>
    <div class="item"><span>辛い鶏つけそば</span><span class="dots"></span><span>¥860</span></div>
  </section>
  <p class="note">※表示価格は全て税込です。持ち帰り容器代を含みます。</p>

  <footer class="footer">
    <div class="footer-shop">濃厚豚骨醤油 らぁ麺ひなた</div>
    <div class="phone">
      <svg width="60" height="60" viewBox="0 0 24 24" aria-hidden="true"><path fill="#ffd400" d="M6.6 10.8a15.1 15.1 0 0 0 6.6 6.6l2.2-2.2c.3-.3.7-.4 1-.2 1.1.4 2.3.6 3.6.6.6 0 1 .4 1 1V20c0 .6-.4 1-1 1A17 17 0 0 1 3 4c0-.6.4-1 1-1h3.5c.6 0 1 .4 1 1 0 1.3.2 2.5.6 3.6.1.3 0 .7-.2 1z"/></svg>
      <span>03-5812-7406</span>
    </div>
    <div class="partner"><div class="name">FoodDashy</div><div class="sub">加盟店</div></div>
    <div class="preorder">お電話で事前注文いただけます</div>
    <div class="address">東京都港区東山崎5-8-41 コルネ台ビル1階　Chirpitアカウント：@noodle_hinata</div>
  </footer>
</main>
</body>
</html>
```